Brisbane IT support business needs our first business card

Hello we are a Brisbane based Information Technology company providing support and services to small and medium sized businesses. We provide a range of services and solutions.

The business name is Wattleridge Computer Services Group, or WCSG for short.

I am looking for a business card that looks professional (don't we all want that), but most importantly, it most utilize the colours in the logo attached.

Other business owners seeking our IT services, and also home users.

Business

• Please only use the blue/orange colours in logo attached

```html
<!DOCTYPE html>
<html lang="en">
<head>
<meta charset="utf-8">
<title>WCSG Business Card</title>
<link href="https://fonts.googleapis.com/css2?family=Ubuntu:wght@400;500;700&display=swap" rel="stylesheet">
<style>
  :root {
    --navy: #0d3551;
    --orange: #f07113;
    --white: #ffffff;
    --skyline: #dcdde0;
    --backdrop: #e9e6e1;
  }
  * { margin: 0; padding: 0; box-sizing: border-box; }
  html, body { width: 1200px; height: 900px; overflow: hidden; }
  body {
    background: var(--backdrop);
    font-family: "Ubuntu", sans-serif;
    position: relative;
  }
  .card {
    position: absolute;
    left: 270px;
    width: 660px;
    height: 378px;
    border-radius: 4px;
    box-shadow: 0 10px 28px rgba(0,0,0,0.22);
    overflow: hidden;
  }
  /* Back side */
  .card-back { top: 46px; background: var(--navy); }
  .back-emblem {
    position: absolute; left: 50%; top: 62px;
    width: 210px; height: 210px; margin-left: -105px;
    border-radius: 50%; background: var(--white);
    display: flex; align-items: center; justify-content: center;
    color: var(--navy); font-weight: 700; font-size: 58px; letter-spacing: 2px;
  }
  .back-url {
    position: absolute; left: 0; right: 0; bottom: 40px;
    text-align: center; color: var(--white);
    font-size: 20px; font-weight: 500; letter-spacing: 0.5px;
  }
  /* Front side */
  .card-front { top: 470px; background: var(--white); }
  .skyline-area {
    position: absolute; left: 0; right: 0; bottom: 0; height: 220px;
    background: linear-gradient(180deg, rgba(220,221,224,0) 0%, rgba(220,221,224,0.55) 45%, var(--skyline) 100%);
  }
  .brand {
    position: absolute; left: 40px; top: 78px;
    display: flex; align-items: center;
  }
  .brand-circle { width: 108px; height: 108px; border-radius: 50%; background: var(--navy); }
  .brand-divider { width: 3px; height: 86px; background: var(--orange); margin: 0 18px; }
  .brand-name { color: var(--orange); font-size: 58px; font-weight: 700; line-height: 0.9; letter-spacing: 1px; }
  .brand-sub {
    color: var(--navy); font-size: 12px; font-weight: 700;
    line-height: 1.05; margin-top: 4px; letter-spacing: 0.3px;
  }
  .person { position: absolute; right: 36px; top: 30px; text-align: right; }
  .person-name { color: var(--orange); font-size: 19px; font-weight: 500; letter-spacing: 0.5px; }
  .person-role { color: var(--navy); font-size: 15px; }
  .contacts { position: absolute; left: 40px; bottom: 28px; list-style: none; }
  .contact {
    display: flex; align-items: center; gap: 16px;
    color: var(--navy); font-size: 20px; font-weight: 500;
    height: 36px;
  }
  .contact-icon {
    width: 28px; height: 28px; background: var(--orange); border-radius: 2px;
    display: flex; align-items: center; justify-content: center;
  }
  .social { position: absolute; right: 34px; top: 166px; text-align: right; }
  .social-label { color: var(--navy); font-size: 22px; font-weight: 500; margin-bottom: 6px; }
  .social-links { display: flex; gap: 8px; justify-content: flex-end; }
  .social-tile { width: 44px; height: 30px; border-radius: 2px; background: var(--navy); }
  .social-tile.accent { background: var(--orange); }
</style>
</head>
<body>
  <section class="card card-back">
    <div class="back-emblem">WCSG</div>
    <p class="back-url">www.wcsg-it.com.au</p>
  </section>

  <section class="card card-front">
    <div class="skyline-area" role="img" aria-label="Faint grey city skyline with bridge"></div>

    <div class="brand">
      <div class="brand-circle"></div>
      <div class="brand-divider"></div>
      <div>
        <div class="brand-name">WCSG</div>
        <div class="brand-sub">WATTLERIDGE COMPUTER<br>SERVICES GROUP</div>
      </div>
    </div>

    <div class="person">
      <div class="person-name">DANIEL HARROW</div>
      <div class="person-role">Manager</div>
    </div>

    <div class="social">
      <div class="social-label">Follow</div>
      <div class="social-links">
        <span class="social-tile"></span>
        <span class="social-tile"></span>
        <span class="social-tile accent"></span>
      </div>
    </div>

    <ul class="contacts">
      <li class="contact">
        <span class="contact-icon">
          <svg width="16" height="16" viewBox="0 0 16 16"><path d="M3 1.5l3 .5 1 3-2 1.5a9 9 0 0 0 4.5 4.5L11 9l3 1 .5 3-2 1.5C7 14 2 9 1.5 3.5z" fill="#fff"/></svg>
        </span>(07) 5550 1234
      </li>
      <li class="contact">
        <span class="contact-icon">
          <svg width="16" height="16" viewBox="0 0 16 16"><path d="M3 1h7l3 3v11H3z" fill="#fff"/><path d="M5 7h6M5 9.5h6M5 12h4" stroke="#f07113" stroke-width="1.2"/></svg>
        </span>(07) 5550 5678
      </li>
      <li class="contact">
        <span class="contact-icon">
          <svg width="18" height="14" viewBox="0 0 18 14"><rect x="1" y="1" width="16" height="12" fill="#fff"/><path d="M1 1l8 6 8-6" fill="none" stroke="#f07113" stroke-width="1.3"/></svg>
        </span>info@wattleridgecsg.com.au
      </li>
      <li class="contact">
        <span class="contact-icon">
          <svg width="16" height="18" viewBox="0 0 16 18"><path d="M8 1a5 5 0 0 1 5 5c0 4-5 9-5 9S3 10 3 6a5 5 0 0 1 5-5z" fill="#fff"/><circle cx="8" cy="6" r="2" fill="#f07113"/></svg>
        </span>Level 12, Harbour Lane, Brisbane, QLD 4000
      </li>
    </ul>
  </section>
</body>
</html>
```